Specialist Medical practice after professional trifold flyer design for patient information brochure

I am the Director of the Hollowbrook Clinic, a specialist medial and surgical practice in Australia. I am after a professional design of a patient information trifold flyer that can be used for web distribution or for commercial printing for upcoming educational event. The design would need to allow change of images and text to be used as template for future topics but have a common brand look across them. Colours would follow the logo, but primarily blue colours for the hollowbrook theme. The inside text needs to be clearly contrasted to the background for easy reading, as often elderly patients. The design would make use of curves or circles, but open for hexagonal, triangle square vector components. I have included an outline for the initial brochure and included images to include. Other stock background images can be used if they increase the impact of the design over included. A winning design is also one that could be modified to a 4 page bi-fold brochure

Target Market(s)

This will be provided to patients in GP practices, podiatry clinics, radiological practices. Aimed at patients to read and be compelled to look to site or get consultation with me

Industry/Entity Type

Medical

Font styles to use
Serif
Sans Serif

Colors
33a6d7
0355a3
86cfc6
cedeed
0292cd
85cae6

Requirements
Must have
• The front cover needs to engage the patient to pick up and read- yes I have a painful ankle and want to find out more. the goal for the inside is to provide the options but be able to direct to website for more info - website currently undergoing upgrade. After professional modern look. Not bright contrasting colours like many advertising brochures. Needs to able to have images and text changed but following same look to create new topics
Nice to have
• The focus is a Tri-fold brochure. Nice to be able to modify to bifold. A winning design would even offer both, or submit separate bifold and trifold. I am open to different versions of similar look. (eg option of brochure with curved elements, triangular or square, or hexagonal.
Should not have
• To many contrasting colours. Text must be easily read on background, either white or coloured background texture with transparency

```html
<!DOCTYPE html>
<html lang="en">
<head>
<meta charset="utf-8">
<title>Ankle Arthritis – Patient Information</title>
<link href="https://fonts.googleapis.com/css2?family=Lato:wght@400;700&display=swap" rel="stylesheet">
<style>
:root{
  --bg:#dcdcdc;
  --paper:#ffffff;
  --ink:#1e1e1e;
  --heading:#8a8a8a;
  --blue-deep:#0355a3;
  --blue:#0292cd;
  --blue-mid:#33a6d7;
  --xray-dark:#0c0c0c;
  --xray-light:#9a9a9a;
}
*{box-sizing:border-box;margin:0;padding:0}
html,body{width:1200px;height:800px;overflow:hidden;background:var(--bg)}
body{display:flex;align-items:center;justify-content:center;font-family:'Lato',sans-serif;color:var(--ink)}
.brochure-inside{display:flex;width:984px;height:760px;background:var(--paper);position:relative;box-shadow:0 6px 18px rgba(0,0,0,.18)}
.brochure-inside::after{content:"";position:absolute;left:0;right:0;bottom:0;height:9px;background:linear-gradient(90deg,var(--blue-deep),var(--blue))}
.panel{width:328px;height:100%;padding:42px 28px 0;position:relative;border-right:1px solid #eee}
.panel:last-child{border-right:none}
.body-text{font-size:10.6px;line-height:1.32;margin-bottom:11px;text-align:justify}
.section-title{font-size:15px;font-weight:400;color:var(--heading);padding-bottom:4px;margin:16px 0 9px;position:relative;display:inline-block}
.section-title::after{content:"";position:absolute;left:0;bottom:0;width:100%;height:2px;background:linear-gradient(90deg,var(--blue-deep),var(--blue-mid))}
.web-link{font-size:12.5px;color:var(--blue);line-height:1.3;margin-top:12px}
.xray{position:relative;width:250px;height:172px;margin:18px auto 0}
.xray svg{width:100%;height:100%;display:block}
.desk-photo{position:absolute;left:0;right:0;bottom:9px;height:250px;background:linear-gradient(180deg,#f3f2f0 0%,#d9dde3 45%,#8fa0b8 75%,#3f5d8a 100%)}
</style>
</head>
<body>
<main class="brochure-inside">

  <section class="panel panel-intro">
    <p class="body-text">Ankle arthritis is a painful condition where there is loss of cartilage from the ankle joint surface. Although not as common as knee or hip arthritis, pain can be debilitating affecting quality of life.</p>
    <p class="body-text">Arthritis of the joint can be caused by trauma joint such as fracture or recurrent instability or secondary from inflammatory conditions such as rheumatoid arthritis.</p>
    <p class="body-text">Pain from the joint will occur with activity causing a limp, limiting walking speed and distance. Often there is swelling of the joint with progressive loss of motion.</p>
    <p class="body-text">Diagnosis is made with examination of the ankle and weight bearing x-rays showing loss of joint space.</p>
    <div class="xray" role="img" aria-label="X-ray of an arthritic ankle joint">
      <svg viewBox="0 0 250 172">
        <defs><radialGradient id="x1" cx="55%" cy="45%" r="60%"><stop offset="0" stop-color="#9a9a9a"/><stop offset=".6" stop-color="#4a4a4a"/><stop offset="1" stop-color="#0c0c0c"/></radialGradient></defs>
        <path d="M18 150 A118 92 0 0 1 236 120" fill="none" stroke="#0355a3" stroke-width="5" transform="rotate(180 125 86)"/>
        <ellipse cx="130" cy="82" rx="112" ry="80" fill="url(#x1)"/>
      </svg>
    </div>
    <div class="desk-photo" role="img" aria-label="Photo of a stethoscope resting on a laptop keyboard while a doctor writes notes"></div>
  </section>

  <section class="panel panel-fusion">
    <p class="body-text">When pain medication, activity modification and shoe wear modification is no longer effective to control the pain then it is worthwhile discussing with your GP for referral to Dr Martin Ellery for an opinion on further treatment. As an Orthopaedic Foot and Ankle surgeon, he will be able to assess your conditions and give advice on the best options for your treatment.</p>
    <p class="body-text">The decision on the best option is based on your age, activity level, existing medical problems, previous ankle treatment and your expected outcome from treatment. In the situation of end stage arthritis options consist of either Ankle fusion or Total Ankle replacement.</p>
    <h2 class="section-title">Ankle Fusion Surgery</h2>
    <p class="body-text">This operation aims to stiffen the ankle joint by fusing the tibia and talus together in the optimal position for function. The common thought is that there will be no movement of the foot, and the patient will walk with a limp. The fusion only occurs at the ankle joint, leaving motion available to the surrounding joints. Although there is decreased motion, you will walk more normally after a fusion without a limp as the pain to the joint is removed.</p>
    <p class="web-link">For more information on ankle fusion, risks and recovery visit our website:<br>www.hollowbrookclinic.com.au/Ankle-Fusion</p>
    <div class="xray" role="img" aria-label="X-ray of an ankle fused with screws and a plate">
      <svg viewBox="0 0 250 172">
        <defs><radialGradient id="x2" cx="50%" cy="40%" r="60%"><stop offset="0" stop-color="#a8a8a8"/><stop offset=".6" stop-color="#4a4a4a"/><stop offset="1" stop-color="#0c0c0c"/></radialGradient></defs>
        <path d="M10 60 A118 92 0 0 0 240 110" fill="none" stroke="#0292cd" stroke-width="5"/>
        <ellipse cx="125" cy="82" rx="112" ry="80" fill="url(#x2)"/>
      </svg>
    </div>
  </section>

  <section class="panel panel-replacement">
    <h2 class="section-title" style="margin-top:0">Total Ankle Replacement Surgery</h2>
    <p class="body-text">In suitable patients there may be the option to maintain joint motion and perform a Total Ankle Replacement. Like a hip or knee replacement operation, the arthritic joint is removed and replaced with an artificial joint. Like an ankle fusion there will be alleviation of the pain and limp with maintenance of the ankle joint motion. Recovery to walking post-surgery is often much sooner than with ankle fusion. Dr Martin Ellery is one of the few surgeons to have completed an international fellowship in ankle replacement surgery and has been performing the technique since 2008. He is currently performing the technique using the Meridian Total ankle with Guidepath guides.</p>
    <p class="web-link">For more information on ankle fusion, risks and recovery visit our website:<br>www.hollowbrookclinic.com.au/Ankle-Replacement</p>
    <div class="xray" role="img" aria-label="X-ray of an ankle with a total ankle replacement implant">
      <svg viewBox="0 0 250 172">
        <defs><radialGradient id="x3" cx="45%" cy="45%" r="60%"><stop offset="0" stop-color="#a0a0a0"/><stop offset=".6" stop-color="#4a4a4a"/><stop offset="1" stop-color="#0c0c0c"/></radialGradient></defs>
        <path d="M12 110 A118 92 0 0 0 240 70" fill="none" stroke="#0355a3" stroke-width="5"/>
        <ellipse cx="125" cy="82" rx="112" ry="80" fill="url(#x3)"/>
      </svg>
    </div>
    <h2 class="section-title">Results of surgery</h2>
    <p class="body-text">Successful surgery in the suitable patient will help resolve the pain associated with the ankle arthritis. Ankle Fusion surgery is ideal for patients with heavy labour work, allowing them to return to previous activities. There may be the risk of arthritis to surrounding joints in the future, but often this occurs many years down the track. Results from Total Ankle replacement surgery have been improving over the years, but there is known risks of loosening, cyst formation or failure of the joint over time that can occur in some patients. It is important to have a opinion from an Orthopaedic Foot and Ankle Surgeon experienced in the these procedure to determine which procedure will provide the best long term solution for you.</p>
  </section>

</main>
</body>
</html>
```